Larkfield Rowhomes - Billboard design for our newly renovated townhome community

We have a 5' wide x 4' tall billboard at the entrance to our apartment community, that needs to have the acrylic insert replaced. It is a 2 sided sign, and we are planning to use the same image on both sides. We are called Larkfield Rowhomes, and have 48 townhomes that are all 2 bedroom, 1 1/2 bath. A few things we would like to get across on the signage: "Newly Renovated" "2 bed 1 1/2 bath" "Full size W/D in every home" " New Appliances" I've included our parent company's logo - this is the only image I could think of, but it might not be worth having it on the sign. We are in Colorado, so mountain theme could be nice and also sunshine/sun since we are called "Larkfield"

Industry/Entity Type

Apartment

Font styles to use
Sans Serif

Requirements
Must have
• Newly Renovated
2 bed 1 1/2 bath
Full size W/D in every home
Virtual Tours available
www.brambletonhomesco.example
855 - 413 - 9286
Nice to have
• We are located in Colorado - possibly mountain theme? Since our community is called "Larkfield Rowhomes" - anything bright with Sun / Sunshine might look really nice as well.

```html
<!DOCTYPE html>
<html lang="en">
<head>
<meta charset="utf-8">
<title>Larkfield Rowhomes</title>
<link rel="stylesheet" href="https://fonts.googleapis.com/css2?family=Arimo:wght@700&display=swap">
<style>
  :root {
    --brand-blue: #1d4f9e;
    --deep-blue: #123a7a;
    --sun-yellow: #ffe81a;
    --sky-top: #6fa5dc;
    --sky-mid: #b9cfe6;
    --glow: #f6c79a;
    --ember: #e98d55;
    --peak: #5d6f92;
    --ridge: #2b3a55;
    --halo: rgba(255,255,255,0.85);
  }
  html, body {
    margin: 0;
    padding: 0;
    width: 1200px;
    height: 949px;
    overflow: hidden;
    background: #ffffff;
  }
  .billboard {
    position: relative;
    width: 1200px;
    height: 949px;
    overflow: hidden;
    font-family: "Arimo", Arial, sans-serif;
    font-weight: 700;
  }
  .scenery {
    position: absolute;
    inset: 0;
    background: linear-gradient(180deg,
      var(--sky-top) 0%,
      var(--sky-mid) 22%,
      #dcdce6 38%,
      var(--glow) 52%,
      var(--ember) 63%,
      #d9a78a 70%,
      var(--peak) 78%,
      var(--ridge) 92%,
      #1c2638 100%);
  }
  .corner-banner {
    position: absolute;
    left: 0;
    top: 0;
    width: 500px;
    height: 340px;
  }
  .corner-banner__text {
    position: absolute;
    left: 10px;
    top: 105px;
    width: 340px;
    transform: rotate(-33.7deg);
    transform-origin: center;
    text-align: center;
    font-variant: small-caps;
    color: var(--sun-yellow);
    font-size: 50px;
    line-height: 52px;
  }
  .heading {
    position: absolute;
    margin: 0;
    font-variant: small-caps;
    color: var(--brand-blue);
    text-shadow: 0 0 6px var(--halo), 0 0 2px var(--halo);
    white-space: nowrap;
  }
  .title {
    right: 36px;
    top: 36px;
    text-align: right;
    font-size: 108px;
    line-height: 104px;
    letter-spacing: -1px;
  }
  .title span { display: block; }
  .unit-spec {
    left: 0;
    right: 0;
    text-align: center;
    font-size: 82px;
    line-height: 88px;
  }
  .unit-spec--beds { top: 282px; padding-left: 80px; }
  .unit-spec--baths { top: 376px; padding-left: 60px; }
  .feature {
    left: 0;
    right: 0;
    text-align: center;
    font-size: 48px;
    line-height: 54px;
  }
  .feature--laundry { top: 486px; }
  .feature--appliances { top: 546px; }
  .tours {
    position: absolute;
    left: 0;
    right: 0;
    top: 618px;
    margin: 0;
    text-align: center;
    font-size: 36px;
    line-height: 42px;
    color: var(--deep-blue);
    text-shadow: 0 0 6px var(--halo), 0 0 2px var(--halo);
  }
  .tours span { margin: 0 18px; }
  .phone {
    position: absolute;
    left: 0;
    right: 0;
    top: 700px;
    margin: 0;
    text-align: center;
    font-size: 176px;
    line-height: 180px;
    letter-spacing: -4px;
    color: var(--sun-yellow);
    -webkit-text-stroke: 5px var(--deep-blue);
    paint-order: stroke fill;
  }
</style>
</head>
<body>
<main class="billboard">
  <div class="scenery" role="img" aria-label="Photo of a golden sunset sky with glowing clouds over snow-dusted Colorado mountain peaks"></div>

  <div class="corner-banner">
    <svg width="500" height="340" viewBox="0 0 500 340" aria-hidden="true">
      <polygon points="0,132 330,0 495,0 0,330" fill="var(--brand-blue)"/>
    </svg>
    <div class="corner-banner__text">Newly<br>Renovated</div>
  </div>

  <h1 class="heading title"><span>Larkfield</span><span>Rowhomes</span></h1>

  <p class="heading unit-spec unit-spec--beds">2 BEDROOMS</p>
  <p class="heading unit-spec unit-spec--baths">1½&nbsp; BATHS</p>

  <p class="heading feature feature--laundry">FULL SIZE W/D in EVERY HOME</p>
  <p class="heading feature feature--appliances">NEW APPLIANCES</p>

  <p class="tours"><span>Virtual Tours Available</span><span>www.brambletonhomesco.example</span></p>

  <p class="phone">855-413-9286</p>
</main>
</body>
</html>
```